New Custom Pizza Box Design Project For Independant Restaurant

We are looking for creative designs for our new custom printed pizza boxes. Designs should include the following:

-Our logo & company name
-A color scheme similar to our current logo
-Our physical and URL addresses & phone number (menu is attached)
-Ability to scale the design across several box sizes (10x10x2, 14x14x2, 18x13x2,
26x18x2)
- Any creative flair you think will make for the best design

Design can be on a white or kraft (tan) box.
Designs can be either two or three ink colors.

***Please note, designs must be able to be screen printed on boxes***
Updates

Reason: Still debating which to choose

Target Market(s)

Industry/Entity Type

Pizza Delivery

Font styles to use
Other font styles liked:
• Please use font similar to our logo text

Requirements
Must have
• -2 or 3 ink colors
• -company name, address, phone number, URL
• -company logo and colors
• -flexibility to use on different box sizes (10x10x2, 14x14x2, 18x13x2,
• 26x18x2)
• -utilize full printable area on boxes (including 2" dimension on box sides)
• ***Please note, designs must be able to be screen printed on boxes***
Should not have
• Design features with strong similarities to existing designs of other pizzerias

```html
<!DOCTYPE html>
<html lang="en">
<head>
<meta charset="utf-8">
<title>Marco's Henhouse Pizzeria – Box Lid</title>
<link rel="stylesheet" href="https://fonts.googleapis.com/css2?family=Oswald:wght@500;600&display=swap">
<style>
  :root {
    --kraft-brown: #6c4a34;
    --ribbon-yellow: #e6b21b;
    --stitch: #33241b;
    --ink-white: #ffffff;
    --ink-yellow: #e4aa16;
  }
  html, body {
    margin: 0;
    padding: 0;
    overflow: hidden;
  }
  .box-lid {
    position: relative;
    width: 1200px;
    height: 1200px;
    overflow: hidden;
    background:
      repeating-linear-gradient(0deg, rgba(0,0,0,0.05) 0 1px, transparent 1px 4px),
      var(--kraft-brown);
    font-family: 'Oswald', 'Arial Narrow', sans-serif;
  }
  .ribbon {
    position: absolute;
    left: 0;
    top: 0;
    width: 1200px;
    height: 1200px;
  }
  .brand-name {
    margin: 0;
    font-weight: 600;
  }
  .brand-line {
    position: absolute;
    left: 355px;
    width: 564px;
    margin: 0;
    text-align: center;
    color: var(--ink-white);
    text-transform: uppercase;
    line-height: 1;
  }
  .line-owner { top: 172px; font-size: 80px; letter-spacing: 4px; }
  .line-main { top: 282px; font-size: 112px; letter-spacing: 5px; }
  .line-trade { top: 560px; font-size: 80px; letter-spacing: 4px; }
  .brand-emblem {
    position: absolute;
    left: 557px;
    top: 396px;
    width: 160px;
    height: 160px;
    border-radius: 50%;
    background: var(--ink-white);
  }
  .contact {
    position: absolute;
    left: 0;
    width: 1200px;
    top: 1018px;
    margin: 0;
    text-align: center;
    font-weight: 500;
    line-height: 1.05;
  }
  .contact .web {
    display: block;
    color: var(--ink-yellow);
    font-size: 56px;
  }
  .contact .phone {
    display: block;
    color: var(--ink-white);
    font-size: 60px;
  }
</style>
</head>
<body>
<main class="box-lid">
  <svg class="ribbon" viewBox="0 0 1200 1200" aria-hidden="true">
    <polygon points="355,0 919,0 919,936 637,808 355,918" fill="var(--ribbon-yellow)"/>
    <g fill="none" stroke="var(--stitch)" stroke-width="3" stroke-dasharray="10 5">
      <polyline points="336,0 336,968 637,830 938,968 938,0"/>
      <polyline points="344,0 344,960 637,822 930,960 930,0"/>
    </g>
  </svg>

  <h1 class="brand-name">
    <span class="brand-line line-owner">Marco's</span>
    <span class="brand-line line-main">Henhouse</span>
    <span class="brand-line line-trade">Pizzeria</span>
  </h1>
  <div class="brand-emblem" role="img" aria-label="Brand emblem: rooster with cutlery and pizza slice"></div>

  <p class="contact">
    <span class="web">WWW.HENHOUSEPIZZA.COM</span>
    <span class="phone">Call us on +01 555 0199</span>
  </p>
</main>
</body>
</html>
```